依頼詳細
◇サイトマップ
①Home ※メニューページ・代表あいさつ・アクセス・ブログレコメンド SNSはリンク・無料相談を打ち出す
② 選ばれる理由※コンセプト
③ 事業案内
④ 事業所概要
⑤ 料金 ※相談無料・その他料金
⑥ よくある質問 ※カテゴリ分け
⑦ お問い合わせ ※お問い合わせフォーム
⑧代表紹介
⑨ブログ(一覧・詳細) ※サイト内ブログ・カテゴリ作成
⑩ニュース(一覧・詳細) ※サイト内ブログ
⑪ 不動産登記
⑫相続
⑬遺言
⑭成年後見
⑮ 家族信託
⑯商業登記
⑰お客様の声 ※アンケート
⑱ビジネスパートナー ※項目名は変える

◇優先事項
1.ユーザビリティー
2.凝ったデザイン
3.編集更新

◇期待する効果
1.売上の向上
2.新規顧客の獲得
3.問い合わせ数の向上

◇ターゲット
【性別】男女比(男6 : 4女)
【年代】30代~50代
【属性】会社員 自営業(経営者) その他として士業の方

◇sns
Instagram  個人用
Facebook  会社用
Twitter   会社用
LINE 今後やるかも

◇テイスト
ナチュラル 優しい 清潔感
サイトURL
http://k-tomoe.net/index.html
ページ数
1ページ
希望イメージ
シンプル 複雑
単色 カラフル
暗い 明るい
日常 高級
遊び心 厳粛
未来的 伝統的
女性的 男性的
希望する色
青系、ベースは白系が良いです。 水色 グレー系やミドリ系があっても良いかも。
納品ファイル
• イラストレーター形式 (.ai)
• フォトショップ形式 (.psd)
• PNG形式 (.png)
補足説明
素材①
店内写真などをベルトラックスを使って、アップしています。
下記URLよりダウンロードしてください。
■ダウンロードURL:http://beltrax.jp/download/4c81e02b9d3f6a17e5b0c2d8a94f61e3b07d5c29
ダウンロードパスワード pass

素材②
ピクモル:https://jp.picmolle.com/
当社で定期契約をしています。クレジット購入のみのもの以外をご利用下さい。
また定期契約のものは弊社の負担となり、ランサー様に負担はありません。
カンプ画像を入れてください。

素材③
現行サイトより引用してください。
URL:http://k-tomoe.net/index.html
画像やテキストに関しては一旦引き抜いて頂いて構いません。
延長を行わせて頂きます。
宜しくお願いたします。
提案を延長させて頂きます。
理由として、全体のテイストが、いかにも、司法書士事務所のという感じで、
なんとなく近寄りがたい印象があります・・

https://meigawari.sitebako.com/
上記のようなイメージでお願いできればと思います。

https://www.kogure-hoki.com/index.html
上記のサイトになるとやりすぎている印象はありますが、テイストとして取り入れて頂きたいです。
現状の経営理念に近い考え方が「今を楽しみ、未来につなぐ」になるため、デザイン作成時に参考にして頂ければと思います!

デザインがイメージ通りに上がってきた為、選定をさせた頂きました。
修正の対応も丁寧にまとめていただいたり、適切な質問を頂き非常に進行が行いやすかったです。
ありがとうございました。

途中でテイストが変わってしまいましたが、お付き合い頂いたランサー様が多く非常に助かりました。感謝致します。
選定出来なかった皆様にこころ苦しい気持ちでいっぱいです。
ありがとうございました。

```html
<!DOCTYPE html>
<html lang="ja">
<head>
<meta charset="utf-8">
<title>朝霧法務司法書士事務所</title>
<link rel="stylesheet" href="https://fonts.googleapis.com/css2?family=Noto+Sans+JP:wght@400;500;700&family=Noto+Serif+JP:wght@500;600&display=swap">
<style>
:root{
  --blue:#2d63ad;
  --navy:#1d3b6e;
  --sky:#e8f0f9;
  --gray:#eef0f3;
  --line:#d6dbe3;
  --text:#333a45;
  --muted:#6b7482;
  --orange:#f4a326;
  --white:#ffffff;
}
*{margin:0;padding:0;box-sizing:border-box}
html,body{width:1200px;height:3448px;overflow:hidden}
body{font-family:"Noto Sans JP",sans-serif;color:var(--text);background:var(--white);font-size:14px;line-height:1.8}
.brand{display:flex;align-items:center;gap:10px;color:var(--navy)}
.brand-mark{width:30px;height:30px;border-radius:50%;background:var(--blue)}
.brand-name{font-size:22px;font-weight:700;letter-spacing:.04em}
.brand-sub{font-size:10px;letter-spacing:.2em;color:var(--muted);display:block}

.hero{position:relative;height:630px;background:linear-gradient(180deg,#f4f6f9,#e9edf2)}
.hero .brand{position:absolute;left:40px;top:28px}
.hero-photo{position:absolute;right:0;top:0;width:640px;height:630px;background:linear-gradient(120deg,#c8d2de,#7d8c9e 60%,#44505f)}
.hero-tiles{position:absolute;left:0;top:0;width:230px;height:260px;background:linear-gradient(135deg,#6a8fc0,#b8cbe2)}
.hero-copy{position:absolute;left:190px;top:250px}
.hero-copy h1{font-family:"Noto Serif JP",serif;font-weight:600;font-size:44px;line-height:1.55;color:#2a3340;letter-spacing:.08em}
.hero-copy h1 span{display:block}
.hero-copy h1 span+span{padding-left:60px}
.hero-copy p{margin-top:18px;font-size:14px;color:var(--blue)}

.nav{position:absolute;left:0;right:0;top:630px;height:52px;background:var(--white);display:flex;justify-content:center;align-items:center;gap:34px;box-shadow:0 2px 8px rgba(0,0,0,.06);z-index:2}
.nav a{font-size:13px;color:var(--text);text-decoration:none}
.nav a.current{color:var(--blue);font-weight:700}
.nav .cta{background:var(--orange);color:var(--white);padding:8px 26px;border-radius:20px;font-weight:700}

.greeting{position:absolute;top:682px;left:0;width:1200px;height:300px;background:linear-gradient(90deg,#3d70b6,#5d8dcc)}
.greeting-photo{position:absolute;left:80px;top:20px;width:300px;height:280px;background:linear-gradient(180deg,#9fb5d2,#2c3e5a)}
.greeting-body{position:absolute;left:440px;top:46px;width:680px;color:var(--white)}
.greeting-body h2{font-size:22px;font-weight:700;letter-spacing:.1em}
.greeting-body small{display:block;font-size:11px;opacity:.8;margin-bottom:12px}
.greeting-body p{font-size:13px;line-height:2;opacity:.95}

.section{position:absolute;left:0;width:1200px;text-align:center}
.section-title{display:flex;flex-direction:column;align-items:center;gap:6px;margin-bottom:36px}
.section-title i{width:12px;height:12px;background:var(--blue);transform:rotate(45deg)}
.section-title h2{font-size:20px;font-weight:700;letter-spacing:.12em;color:var(--navy)}
.more{display:inline-block;background:var(--navy);color:var(--white);font-size:13px;padding:10px 60px;border-radius:22px;text-decoration:none}

.reasons{top:1030px;height:360px}
.reason-list{display:flex;justify-content:center;gap:30px;margin-bottom:40px}
.reason{width:300px;text-align:left}
.reason-photo{height:120px;background:linear-gradient(135deg,#c9d6e6,#8fa6c5);position:relative}
.reason-photo span{position:absolute;left:0;right:0;bottom:0;background:rgba(45,99,173,.9);color:var(--white);font-size:13px;text-align:center;padding:4px}
.reason p{font-size:12px;color:var(--muted);margin-top:12px}

.business{top:1400px;height:640px;background:var(--gray)}
.business-photo{height:150px;background:linear-gradient(180deg,#c6ccd4,#eef0f3)}
.business .section-title{margin-top:-40px}
.biz-grid{display:grid;grid-template-columns:repeat(3,300px);gap:44px 40px;justify-content:center;margin-bottom:40px;text-align:left}
.biz{display:flex;gap:16px}
.biz-icon{flex:none;width:66px;height:66px;border-radius:50%;background:var(--white);display:flex;align-items:center;justify-content:center}
.biz h3{font-size:16px;color:var(--blue);font-weight:700}
.biz p{font-size:11px;color:var(--muted);line-height:1.7}

.office{top:2080px;height:760px}
.map{position:absolute;top:100px;left:0;width:1200px;height:380px;background:linear-gradient(135deg,#e3e6ea,#cfd8e2 50%,#a9c6dd)}
.office-info{position:absolute;top:510px;left:130px;width:470px;text-align:left;font-size:12px}
.office-info dl{display:grid;grid-template-columns:90px 1fr;row-gap:10px}
.office-info dt{font-weight:700;color:var(--navy)}
.contact{position:absolute;top:510px;left:650px;width:420px;text-align:left}
.contact h3{font-size:14px;color:var(--navy)}
.tel{display:flex;align-items:center;gap:8px;font-size:28px;font-weight:700;color:var(--navy);line-height:1.3}
.contact .btn{display:block;background:var(--orange);color:var(--white);text-align:center;padding:8px;font-size:13px;font-weight:700;margin:10px 0;width:340px}
.contact p{font-size:11px;color:var(--muted)}

.news{top:2860px;height:330px}
.news-list{width:940px;margin:0 auto 34px;text-align:left;list-style:none}
.news-list li{display:flex;gap:24px;border-bottom:1px solid var(--line);padding:14px 6px;font-size:13px}
.news-list time{color:var(--blue);font-weight:500}

.pagetop{position:absolute;top:3198px;left:0;width:1200px;height:22px;text-align:center;font-size:10px;color:var(--muted);letter-spacing:.2em}
.footer{position:absolute;top:3220px;left:0;width:1200px;height:228px;background:var(--navy);color:var(--white)}
.footer-links{position:absolute;left:110px;top:30px;display:grid;grid-template-columns:repeat(3,170px);font-size:12px;line-height:2.1;list-style:none}
.footer-links li::before{content:"› ";opacity:.7}
.footer .brand{position:absolute;left:650px;top:34px;color:var(--white)}
.footer .brand-sub{color:#b9c7dc}
.footer-address{position:absolute;left:650px;top:88px;font-size:12px;line-height:1.9}
.footer-address .tel{color:var(--white);font-size:20px}
.copy{position:absolute;bottom:0;left:0;right:0;text-align:center;font-size:10px;background:#16305c;padding:4px}
</style>
</head>
<body>

<header class="hero">
  <div class="hero-tiles" role="img" aria-label="オフィスビルの写真タイル"></div>
  <div class="brand"><span class="brand-mark"></span><div><span class="brand-sub">ASAGIRI LAW OFFICE</span><span class="brand-name">朝霧法務司法書士事務所</span></div></div>
  <div class="hero-photo" role="img" aria-label="笑顔で話す代表司法書士の写真"></div>
  <div class="hero-copy">
    <h1><span>「何でも話せる」</span><span>存在でありたい</span></h1>
    <p>コミュニケーションを大切に、どんなことでもお気軽にご相談ください。</p>
  </div>
</header>

<nav class="nav">
  <a class="current" href="#">HOME</a><a href="#">代表あいさつ</a><a href="#">選ばれる理由</a><a href="#">事業案内</a><a href="#">料金</a><a href="#">よくある質問</a><a class="cta" href="#">お問い合わせ</a>
</nav>

<section class="greeting">
  <div class="greeting-photo" role="img" aria-label="本を手にした代表の写真"></div>
  <div class="greeting-body">
    <h2>代表あいさつ</h2>
    <small>GREETING</small>
    <p>当事務所のホームページをご覧いただき、誠にありがとうございます。私たちは「今を楽しみ、未来につなぐ」を理念に、お客様一人ひとりのお話に丁寧に耳を傾けてまいります。相続や不動産登記、会社の手続きなど、身近なお悩みをわかりやすくご説明し、安心して次の一歩を踏み出せるようお手伝いいたします。どんな小さなことでもお気軽にご相談ください。</p>
  </div>
</section>

<section class="section reasons">
  <div class="section-title"><i></i><h2>選ばれる理由</h2></div>
  <div class="reason-list">
    <div class="reason"><div class="reason-photo" role="img" aria-label="相談風景の写真"><span>相談は無料、安心できる</span></div><p>初回のご相談は無料です。費用のことも事前に丁寧にご説明いたします。</p></div>
    <div class="reason"><div class="reason-photo" role="img" aria-label="打ち合わせの写真"><span>土日祝日にも対応</span></div><p>お仕事でお忙しい方にも、ご都合に合わせて柔軟に対応いたします。</p></div>
    <div class="reason"><div class="reason-photo" role="img" aria-label="握手する手元の写真"><span>他士業との連携で一括対応</span></div><p>税理士などと連携し、ワンストップで手続きをサポートします。</p></div>
  </div>
  <a class="more" href="#">もっと詳しく</a>
</section>

<section class="section business">
  <div class="business-photo" role="img" aria-label="書類とパソコンが並ぶデスクの写真"></div>
  <div class="section-title"><i></i><h2>事業案内</h2></div>
  <div class="biz-grid">
    <div class="biz"><span class="biz-icon"><svg width="30" height="30" viewBox="0 0 30 30"><path d="M4 15 15 5l11 10v11H4z" fill="none" stroke="#2d63ad" stroke-width="2"/></svg></span><div><h3>不動産登記</h3><p>売買・贈与・住宅ローン完済時の抵当権抹消などを行います。</p></div></div>
    <div class="biz"><span class="biz-icon"><svg width="30" height="30" viewBox="0 0 30 30"><circle cx="15" cy="15" r="11" fill="none" stroke="#2d63ad" stroke-width="2"/><path d="M15 15V4a11 11 0 0 1 11 11z" fill="#2d63ad"/></svg></span><div><h3>相続</h3><p>相続登記や遺産分割協議書の作成をサポートいたします。</p></div></div>
    <div class="biz"><span class="biz-icon"><svg width="30" height="30" viewBox="0 0 30 30"><rect x="7" y="4" width="16" height="22" fill="none" stroke="#2d63ad" stroke-width="2"/><path d="M11 11h8M11 16h8M11 21h5" stroke="#2d63ad" stroke-width="2"/></svg></span><div><h3>遺言</h3><p>大切な想いを確実に残すため、遺言書の作成をお手伝いします。</p></div></div>
    <div class="biz"><span class="biz-icon"><svg width="30" height="30" viewBox="0 0 30 30"><circle cx="15" cy="10" r="5" fill="none" stroke="#2d63ad" stroke-width="2"/><path d="M6 26c0-6 4-9 9-9s9 3 9 9" fill="none" stroke="#2d63ad" stroke-width="2"/></svg></span><div><h3>成年後見</h3><p>判断能力が不安な方の財産管理や生活を法的に支えます。</p></div></div>
    <div class="biz"><span class="biz-icon"><svg width="30" height="30" viewBox="0 0 30 30"><path d="M5 25V13l10-8 10 8v12" fill="none" stroke="#2d63ad" stroke-width="2"/><circle cx="15" cy="17" r="3" fill="#2d63ad"/></svg></span><div><h3>家族信託</h3><p>ご家族に財産管理を託す仕組みづくりをご提案します。</p></div></div>
    <div class="biz"><span class="biz-icon"><svg width="30" height="30" viewBox="0 0 30 30"><rect x="5" y="9" width="20" height="15" fill="none" stroke="#2d63ad" stroke-width="2"/><path d="M11 9V6h8v3" fill="none" stroke="#2d63ad" stroke-width="2"/></svg></span><div><h3>商業登記</h3><p>会社設立や役員変更など、法人の登記手続きを行います。</p></div></div>
  </div>
  <a class="more" href="#">もっと詳しく</a>
</section>

<section class="section office">
  <div class="section-title"><i></i><h2>事務所概要</h2></div>
  <div class="map" role="img" aria-label="事務所周辺の地図"></div>
  <div class="office-info">
    <dl>
      <dt>事務所名</dt><dd>朝霧法務司法書士事務所</dd>
      <dt>代表</dt><dd>朝霧 一郎</dd>
      <dt>所在地</dt><dd>〒540-0000<br>大阪府大阪市北浜区北浜1丁目2番3号<br>北浜ビル5階</dd>
      <dt>営業時間</dt><dd>平日 9:00〜18:00（土日祝は要予約）</dd>
    </dl>
  </div>
  <div class="contact">
    <h3>お問い合わせはお気軽に！</h3>
    <div class="tel"><svg width="24" height="24" viewBox="0 0 24 24"><path d="M6 3h4l2 5-3 2a11 11 0 0 0 5 5l2-3 5 2v4c0 1-1 2-2 2A18 18 0 0 1 4 5c0-1 1-2 2-2z" fill="#1d3b6e"/></svg>06-6000-4123</div>
    <a class="btn" href="#">メールでのお問い合わせ</a>
    <p>お電話は平日9時から18時まで受け付けております。<br>メールは24時間受付、翌営業日にご返信いたします。</p>
  </div>
</section>

<section class="section news">
  <div class="section-title"><i></i><h2>NEWS</h2></div>
  <ul class="news-list">
    <li><time>2024.05.20</time><span>ホームページをリニューアルいたしました</span></li>
    <li><time>2024.05.01</time><span>ゴールデンウィーク期間の営業についてのお知らせ</span></li>
    <li><time>2024.04.10</time><span>無料相談会を開催いたします</span></li>
  </ul>
  <a class="more" href="#">もっと詳しく</a>
</section>

<div class="pagetop">▲ PAGE TOP</div>

<footer class="footer">
  <ul class="footer-links">
    <li>HOME</li><li>不動産登記</li><li>お客様の声</li>
    <li>代表あいさつ</li><li>相続</li><li>ブログ</li>
    <li>選ばれる理由</li><li>遺言</li><li>ニュース</li>
    <li>事業案内</li><li>成年後見</li><li>よくある質問</li>
    <li>料金</li><li>家族信託</li><li>お問い合わせ</li>
  </ul>
  <div class="brand"><span class="brand-mark"></span><div><span class="brand-sub">ASAGIRI LAW OFFICE</span><span class="brand-name">朝霧法務司法書士事務所</span></div></div>
  <div class="footer-address">
    〒540-0000<br>大阪府大阪市北浜区北浜1丁目2番3号 北浜ビル5階
    <div class="tel">06-6000-4123</div>
  </div>
  <div class="copy">Copyright © 朝霧法務司法書士事務所 All Rights Reserved.</div>
</footer>

</body>
</html>
```